Real Estate Investment Company Needs A Business Card Designed

I need a business card designed for my use. We are a real estate investment company based in Omaha, Nebraska that specializes in buying, rehabbing and selling single family and multifamily properties. Would love designs that incorporate our logo and colors

Industry/Entity Type

Business

Contact Information for Business Card

Marlow Pettigrew | President & CEO
4837 North 52nd Avenue, Ste 200
Omaha, NE 68214
(402) 555-7428
marlow@quillfenhomes.example
www.QuillfenHomes.example

Font styles to use
Serif

Colors
0255a3
3276b5

Requirements
Must have
• Our logo

```html
<!DOCTYPE html>
<html lang="en">
<head>
<meta charset="utf-8">
<title>Quillfen Homes – Business Card</title>
<link href="https://fonts.googleapis.com/css2?family=Montserrat:wght@700&family=Arimo:wght@400&display=swap" rel="stylesheet">
<style>
  :root {
    --bg: #1b1c20;
    --card: #0c0f18;
    --blue: #3a86d1;
    --blue-deep: #2f72b8;
    --ink: #d6d9df;
    --ink-soft: #b9bdc6;
  }
  * { margin: 0; padding: 0; box-sizing: border-box; }
  html, body { width: 1200px; height: 800px; overflow: hidden; background: var(--bg); }
  .canvas {
    width: 1200px; height: 800px;
    display: flex; flex-direction: column; align-items: center; justify-content: center; gap: 40px;
  }
  .card {
    width: 600px; height: 343px;
    background: var(--card);
    border-radius: 3px;
    position: relative;
    box-shadow: 0 14px 30px rgba(0,0,0,.45);
    font-family: "Arimo", Arial, sans-serif;
    color: var(--ink);
  }

  /* Front */
  .card--front { display: flex; flex-direction: column; align-items: center; justify-content: center; }
  .brand-mark {
    width: 96px; height: 96px; border-radius: 50%;
    border: 4px solid var(--blue);
    margin-bottom: 18px;
  }
  .brand-name {
    font-family: "Montserrat", Arial, sans-serif; font-weight: 700;
    color: var(--blue); letter-spacing: .5px;
  }
  .card--front .brand-name { font-size: 26px; }
  .front-url { margin-top: 44px; font-size: 17px; letter-spacing: 1px; color: var(--ink); }

  /* Back */
  .card--back { padding: 50px 0 0 52px; }
  .card--back .brand-name { font-size: 30px; line-height: 1; }
  .person { margin-top: 40px; }
  .person-name { font-size: 22px; color: var(--blue); line-height: 1.1; }
  .person-title { font-size: 16px; color: var(--ink-soft); margin-top: 2px; }
  .contact-list { list-style: none; margin-top: 22px; font-size: 15px; line-height: 1.45; }
  .contact-list li { display: flex; align-items: center; gap: 8px; }
  .contact-icon { width: 16px; height: 16px; flex: none; }
  .address { margin-top: 18px; font-size: 15px; line-height: 1.45; color: var(--ink); }
  .back-mark {
    position: absolute; right: 46px; top: 56px;
    width: 220px; height: 220px; border-radius: 50%;
    border: 5px solid var(--blue);
  }
</style>
</head>
<body>
<main class="canvas">

  <section class="card card--front" aria-label="Card front">
    <div class="brand-mark"></div>
    <div class="brand-name">QUILLFEN HOMES</div>
    <div class="front-url">www.QuillfenHomes.example</div>
  </section>

  <section class="card card--back" aria-label="Card back">
    <div class="brand-name">QUILLFEN HOMES</div>

    <div class="person">
      <div class="person-name">Marlow Pettigrew</div>
      <div class="person-title">President &amp; CEO</div>
    </div>

    <ul class="contact-list">
      <li>
        <svg class="contact-icon" viewBox="0 0 16 16" aria-hidden="true">
          <circle cx="8" cy="8" r="8" fill="var(--blue)"/>
          <path d="M5 4.5c.6-.4 1.1-.3 1.4.2l.6 1.1c.2.4.1.8-.3 1.1l-.4.3c.4.9 1.1 1.6 2 2l.3-.4c.3-.4.7-.5 1.1-.3l1.1.6c.5.3.6.8.2 1.4-.5.7-1.3 1-2.2.6C7 10.3 5.7 9 5 7.1c-.3-.9-.1-1.9.6-2.3z" fill="var(--card)"/>
        </svg>
        (402) 555-7428
      </li>
      <li>
        <svg class="contact-icon" viewBox="0 0 16 16" aria-hidden="true">
          <circle cx="8" cy="8" r="8" fill="var(--blue)"/>
          <rect x="4" y="5.2" width="8" height="5.6" rx=".6" fill="var(--card)"/>
          <path d="M4.3 5.5 8 8.4l3.7-2.9" stroke="var(--blue)" stroke-width=".9" fill="none"/>
        </svg>
        marlow@quillfenhomes.example
      </li>
      <li>
        <svg class="contact-icon" viewBox="0 0 16 16" aria-hidden="true">
          <circle cx="8" cy="8" r="8" fill="var(--blue)"/>
          <circle cx="8" cy="8" r="4" fill="none" stroke="var(--card)" stroke-width="1"/>
          <ellipse cx="8" cy="8" rx="1.7" ry="4" fill="none" stroke="var(--card)" stroke-width="1"/>
          <path d="M4 8h8" stroke="var(--card)" stroke-width="1"/>
        </svg>
        www.QuillfenHomes.example
      </li>
    </ul>

    <p class="address">4837 North 52nd Avenue, Ste 200<br>Omaha, NE 68214</p>

    <div class="back-mark"></div>
  </section>

</main>
</body>
</html>
```